Beautiful e-comm site for 'roadside farmers stand' online!

Need a logo design and basic e-comm website (super super simple) for new business called Brindlecove. Brindlecove is an online farmers stand where local artisans can sell 'brindlecove' goods directly from their makers!

Looking for something simple, whimsicle and clean! (Ideally with a light grey or perrywinkle and some color mixed in - word 'Brindlecove' in black - can work the pear shape in somewhere but not required!)

Target Market(s)

Hobby shoppers and 'quilo' goers who want a focus on edible things and care about ingredients!

Industry/Entity Type

E-Commerce

Number of Pages Required

2 page

Font styles to use
Decorative
Script

Colors
f3f1f8
ec1f27
cadf82

Requirements
Must have
• - Basic logo
• - Homepage
• - Product Detail Page
• - Be in a responsive, woocommerce or shopify, wordpress theme (will purchase theme after design is approved)
Nice to have
• - Matching check out & cart pages
• - 'About Us' page
• - SEO plugin
Should not have
• A cluttered look/feel.

```html
<!DOCTYPE html>
<html lang="en">
<head>
<meta charset="utf-8">
<title>Brindlecove — Farmers Stand</title>
<link rel="stylesheet" href="https://fonts.googleapis.com/css2?family=Roboto:wght@300;400;500;700&family=Lora:ital@1&display=swap">
<style>
:root{
  --red:#ec1f27;
  --green:#cadf82;
  --lilac:#f3f1f8;
  --ink:#231f20;
  --text:#3a3a3a;
  --muted:#8c8c8c;
  --grey-band:#f5f5f5;
  --card-bg:#f4f3ef;
  --white:#ffffff;
}
*{box-sizing:border-box;margin:0;padding:0}
html,body{width:1200px;height:3468px;overflow:hidden}
body{position:relative;font-family:"Roboto",Arial,sans-serif;color:var(--text);background:var(--white)}
.abs{position:absolute}
svg.ic{display:inline-block;vertical-align:middle}

/* top bar */
.topbar{left:0;top:0;width:1200px;height:32px;background:var(--red);color:var(--white);font-size:12px}
.topbar span{position:absolute;top:9px;display:flex;align-items:center;gap:6px}

/* hero */
.hero{left:0;top:32px;width:1200px;height:541px;background:radial-gradient(ellipse at 30% 30%,#6b4a2c 0%,#3a2618 45%,#1d1510 100%)}
.hero-shade{left:0;top:0;width:1200px;height:541px;background:rgba(0,0,0,.35)}
.logo{left:86px;top:16px;font-weight:700;font-size:30px;color:var(--white);display:flex;align-items:center;gap:10px}
.logo i{display:block;width:14px;height:14px;background:var(--green);border-radius:50%}
.nav{top:20px;font-size:11px;font-weight:500;color:var(--white);letter-spacing:.3px}
.nav.active::after{content:"";position:absolute;left:-4px;right:-4px;top:22px;height:3px;background:var(--red)}
.hero-title{left:0;width:1200px;top:176px;text-align:center;font-size:47px;font-weight:400;color:var(--white);letter-spacing:1px}
.hero-title b{color:var(--red);font-weight:700}
.hero-sub{left:0;width:1200px;top:238px;text-align:center;font-size:14px;color:var(--white)}
.btn-ghost{left:508px;top:290px;width:152px;height:32px;border:1.5px solid var(--white);border-radius:16px;color:var(--white);font-size:12px;font-weight:500;display:flex;align-items:center;justify-content:center;gap:4px}

/* about */
.about-tomato{left:0;top:573px;width:250px;height:100px;background:linear-gradient(90deg,#d9361f,#e8774a 55%,rgba(255,255,255,0))}
.sec-title{left:0;width:1200px;text-align:center;font-size:34px;font-weight:500;color:var(--ink);letter-spacing:2px}
.about-copy{left:165px;top:688px;width:870px;text-align:center;font-size:13.5px;line-height:23px;color:var(--muted)}
.btn-green{height:30px;border-radius:15px;background:var(--green);color:var(--white);font-size:12px;font-weight:500;display:flex;align-items:center;justify-content:center;gap:4px}
.veg-band{left:0;top:786px;width:1200px;height:220px;background:linear-gradient(180deg,rgba(255,255,255,0) 0%,#7aa13a 35%,#d8432a 60%,#f0c02f 80%,#4e7a26 100%)}

/* shop */
.tab{top:1112px;height:26px;border-radius:13px;font-size:11px;color:var(--muted);display:flex;align-items:center;justify-content:center;border:1px solid #e6e6e6;background:var(--white)}
.tab.on{background:var(--green);color:var(--white);border-color:var(--green)}
.prod{width:236px}
.prod .pic{width:236px;height:215px;border-radius:6px 6px 40% 40%/6px 6px 20px 20px}
.prod h3{margin-top:20px;text-align:center;font-size:16px;font-weight:500;color:var(--ink)}
.prod p{margin-top:5px;text-align:center;font-size:12px;font-weight:700;color:var(--red)}
.prod p s{color:#bbb;font-weight:400;margin-left:6px}

/* lists band */
.band{left:0;top:1970px;width:1200px;height:562px;background:var(--grey-band)}
.eyebrow{font-size:9px;letter-spacing:1.5px;color:var(--muted)}
.col-title{font-size:23px;font-weight:700;color:var(--ink)}
.arrows{display:flex;gap:6px}
.arrows i{display:block;width:20px;height:20px;border-radius:50%;background:#e8e8e8;color:#777;font-style:normal;font-size:11px;text-align:center;line-height:20px}
.mini{width:326px;height:104px;background:var(--white);border-radius:4px;box-shadow:0 2px 6px rgba(0,0,0,.06)}
.mini .pic{position:absolute;left:14px;top:12px;width:120px;height:80px;border-radius:40px}
.mini h4{position:absolute;left:160px;top:20px;font-size:15px;font-weight:500;color:var(--ink)}
.mini p{position:absolute;left:160px;top:64px;font-size:12px;font-weight:700;color:var(--red)}

/* newsletter */
.news{left:0;top:2532px;width:1200px;height:231px;background:var(--red)}
.news-title{left:88px;top:82px;font-size:30px;color:var(--white);font-weight:300}
.news-title b{font-weight:700}
.news-input{left:467px;top:74px;width:453px;height:50px;border-radius:25px;background:var(--white);font-size:13px;color:#b4b4b4;padding:17px 24px}
.news-btn{left:939px;top:74px;width:175px;height:50px;border-radius:25px;font-size:13px}

/* testimonial */
.testi{left:88px;top:2682px;width:1026px;height:335px;background:var(--white);border-radius:4px;box-shadow:0 4px 14px rgba(0,0,0,.18)}
.avatar{width:88px;height:88px;border-radius:50%;border:5px solid var(--green);background:radial-gradient(circle at 50% 45%,#e9c8aa,#b88a62)}
.quote{font-family:"Lora",Georgia,serif;font-style:italic;font-size:14.5px;line-height:21px;color:#8a8a8a;width:260px}
.who{font-size:11px;font-weight:500;color:var(--ink);display:flex;align-items:center;gap:6px}
.who i{display:block;width:8px;height:8px;background:var(--green);border-radius:50%}

/* footer */
.footer{left:0;top:3093px;width:1200px;height:310px;background:var(--red);color:var(--white)}
.f-logo{left:82px;top:52px;font-size:30px;font-weight:700;display:flex;align-items:center;gap:10px}
.f-logo i{display:block;width:14px;height:14px;background:var(--white);border-radius:50%}
.f-desc{left:88px;top:98px;width:290px;font-size:11.5px;line-height:17px}
.f-line{left:88px;font-size:11.5px;font-weight:700;display:flex;align-items:center;gap:14px}
.f-head{top:59px;font-size:14px;font-weight:300}
.f-head b{font-weight:700}
.f-list{list-style:none;font-size:11.5px}
.f-list li{height:29px;display:flex;align-items:center;gap:8px}
.f-list li::before{content:"";width:8px;height:8px;border:1.5px solid var(--white);border-radius:50%}
.thumb{width:72px;height:70px}
.bottom{left:0;top:3403px;width:1200px;height:65px;background:var(--ink)}
.copy{left:88px;top:32px;font-size:11.5px;color:#ddd}
.pay{top:32px;width:28px;height:18px;border-radius:3px}
</style>
</head>
<body>

<!-- top bar -->
<div class="abs topbar">
  <span style="left:88px"><svg class="ic" width="14" height="10" viewBox="0 0 14 10"><rect x=".5" y=".5" width="13" height="9" fill="none" stroke="#fff"/><path d="M.5 .5 7 6 13.5 .5" fill="none" stroke="#fff"/></svg>brindlecove @ mailbox.com</span>
  <span style="left:259px"><svg class="ic" width="12" height="12" viewBox="0 0 12 12"><path d="M2 1l2 0 1 3-1.5 1a7 7 0 0 0 3.5 3.5L8 7l3 1v2c0 1-1 1-1 1A9 9 0 0 1 1 2c0 0 0-1 1-1z" fill="#fff"/></svg>024 5550 1234</span>
  <span style="left:826px"><svg class="ic" width="16" height="14" viewBox="0 0 16 14"><path d="M0 1h3l2 8h8l2-6H4" fill="none" stroke="#fff" stroke-width="1.4"/><circle cx="6" cy="12" r="1.3" fill="#fff"/><circle cx="12" cy="12" r="1.3" fill="#fff"/></svg>Add to cart</span>
  <span style="left:931px;top:8px">|</span>
  <span style="left:955px"><svg class="ic" width="14" height="12" viewBox="0 0 14 12"><path d="M6 1h6v10H6M1 6h8M6 3l3 3-3 3" fill="none" stroke="#fff" stroke-width="1.4"/></svg>Login</span>
  <span style="left:1024px;top:8px">|</span>
  <span style="left:1045px"><svg class="ic" width="12" height="12" viewBox="0 0 12 12"><circle cx="6" cy="3.5" r="3" fill="#fff"/><path d="M0 12a6 5 0 0 1 12 0z" fill="#fff"/></svg>Register</span>
</div>

<!-- hero -->
<section class="abs hero" role="img" aria-label="Dark still life of pumpkins, pomegranates and nuts on a wooden table">
  <div class="abs hero-shade"></div>
  <div class="abs logo"><i></i>Brindlecove</div>
  <div class="abs nav active" style="left:781px">HOME</div>
  <div class="abs nav" style="left:858px">PRODUCT DETAIL</div>
  <div class="abs nav" style="left:994px">CONTACT US</div>
  <svg class="abs" style="left:1102px;top:19px" width="13" height="13" viewBox="0 0 13 13"><circle cx="5.5" cy="5.5" r="4.3" fill="none" stroke="#fff" stroke-width="1.8"/><path d="M8.6 8.6 12 12" stroke="#fff" stroke-width="1.8"/></svg>
  <h1 class="abs hero-title">We Sell <b>Best Food Products</b></h1>
  <p class="abs hero-sub">Lorem Ipsum is simply dummy text of the printing and typesetting industry. Lorem Ipsum has been industry's</p>
  <div class="abs btn-ghost">SHOP NOW <span>»</span></div>
</section>

<!-- about -->
<div class="abs about-tomato" role="img" aria-label="Tomatoes and herbs"></div>
<h2 class="abs sec-title" style="top:620px">ABOUT US</h2>
<p class="abs about-copy">It is a long established fact that a reader will be distracted by the readable content of a page when looking at its layout. The point of using Lorem Ipsum is that it has a more-or-less normal distribution of letters, as opposed It is a long established fact that a reader will be distracted by the readable content of a page when looking at its layout. The point of using Lorem Ipsum is that it has a more-or-less normal distribution of etters, as opposed</p>
<div class="abs btn-green" style="left:524px;top:800px;width:152px">SHOP NOW <span>»</span></div>
<div class="abs veg-band" role="img" aria-label="Row of fresh vegetables: peppers, tomatoes, lemons and greens"></div>

<!-- shop -->
<h2 class="abs sec-title" style="top:1055px;font-size:31px">OUR SHOP</h2>
<div class="abs tab" style="left:428px;width:76px">All goods</div>
<div class="abs tab on" style="left:516px;width:104px">Fruits</div>
<div class="abs tab" style="left:640px;width:132px">Vegetables</div>

<div class="abs prod" style="left:88px;top:1188px"><div class="pic" role="img" aria-label="Oranges" style="background:radial-gradient(circle at 50% 55%,#f7931e 0 30%,var(--card-bg) 62%)"></div><h3>Orange</h3><p>$50.00<s>$55.00</s></p></div>
<div class="abs prod" style="left:349px;top:1188px"><div class="pic" role="img" aria-label="Cherries" style="background:radial-gradient(circle at 50% 55%,#a3121c 0 24%,var(--card-bg) 58%)"></div><h3>Cherry</h3><p>$50.00<s>$55.00</s></p></div>
<div class="abs prod" style="left:613px;top:1188px"><div class="pic" role="img" aria-label="Mango" style="background:radial-gradient(circle at 50% 55%,#f4a71d 0 28%,var(--card-bg) 60%)"></div><h3>Mango</h3><p>$50.00<s>$55.00</s></p></div>
<div class="abs prod" style="left:876px;top:1188px"><div class="pic" role="img" aria-label="Red apple" style="background:radial-gradient(circle at 50% 55%,#d81e25 0 28%,var(--card-bg) 60%)"></div><h3>Apple</h3><p>$50.00<s>$55.00</s></p></div>

<div class="abs prod" style="left:88px;top:1521px"><div class="pic" role="img" aria-label="Pomegranates" style="background:radial-gradient(circle at 50% 55%,#b3202b 0 28%,var(--card-bg) 60%)"></div><h3>Pomegranate</h3><p>$50.00<s>$55.00</s></p></div>
<div class="abs prod" style="left:349px;top:1521px"><div class="pic" role="img" aria-label="Pineapple" style="background:radial-gradient(circle at 50% 55%,#e8b526 0 26%,#3f7d2c 40%,var(--card-bg) 62%)"></div><h3>Pineapple</h3><p>$50.00<s>$55.00</s></p></div>
<div class="abs prod" style="left:613px;top:1521px"><div class="pic" role="img" aria-label="Bunch of grapes" style="background:radial-gradient(circle at 50% 55%,#4a2344 0 28%,var(--card-bg) 60%)"></div><h3>Grapes</h3><p>$50.00<s>$55.00</s></p></div>
<div class="abs prod" style="left:876px;top:1521px"><div class="pic" role="img" aria-label="Strawberries" style="background:radial-gradient(circle at 50% 55%,#e02a2e 0 28%,var(--card-bg) 60%)"></div><h3>Strawberries</h3><p>$50.00<s>$55.00</s></p></div>

<div class="abs btn-green" style="left:520px;top:1853px;width:158px">VIEW MORE <span>»</span></div>

<!-- lists -->
<section class="abs band">
  <div class="abs eyebrow" style="left:88px;top:60px">NEW FROM THE FARM</div>
  <div class="abs col-title" style="left:88px;top:73px">NEW ARRIVALS</div>
  <div class="abs arrows" style="left:356px;top:76px"><i>‹</i><i>›</i></div>
  <div class="abs eyebrow" style="left:437px;top:60px">BEST SELLER</div>
  <div class="abs col-title" style="left:437px;top:73px">POPULAR</div>
  <div class="abs arrows" style="left:704px;top:76px"><i>‹</i><i>›</i></div>
  <div class="abs eyebrow" style="left:793px;top:60px">CUSTOMER NEEDS</div>
  <div class="abs col-title" style="left:793px;top:73px">Random</div>
  <div class="abs arrows" style="left:1060px;top:76px"><i>‹</i><i>›</i></div>

  <div class="abs mini" style="left:88px;top:127px"><div class="pic" role="img" aria-label="Blackberries" style="background:radial-gradient(#1f1a24 40%,var(--white) 72%)"></div><h4>Blackberry</h4><p>$50.00</p></div>
  <div class="abs mini" style="left:88px;top:259px"><div class="pic" role="img" aria-label="Peach" style="background:radial-gradient(#f08a3a 40%,var(--white) 72%)"></div><h4>Peach</h4><p>$50.00</p></div>
  <div class="abs mini" style="left:88px;top:393px"><div class="pic" role="img" aria-label="Red berries" style="background:radial-gradient(#8e1120 40%,var(--white) 72%)"></div><h4>Redberry</h4><p>$50.00</p></div>

  <div class="abs mini" style="left:439px;top:127px"><div class="pic" role="img" aria-label="Strawberry" style="background:radial-gradient(#e02a2e 40%,var(--white) 72%)"></div><h4>Strawberry</h4><p>$50.00</p></div>
  <div class="abs mini" style="left:439px;top:259px"><div class="pic" role="img" aria-label="Mushrooms" style="background:radial-gradient(#e7ddd0 40%,var(--white) 72%)"></div><h4>Mushroom</h4><p>$50.00</p></div>
  <div class="abs mini" style="left:439px;top:393px"><div class="pic" role="img" aria-label="Apple" style="background:radial-gradient(#d81e25 34%,var(--white) 64%)"></div><h4>Apple</h4><p>$50.00</p></div>

  <div class="abs mini" style="left:791px;top:127px"><div class="pic" role="img" aria-label="Grapes" style="background:radial-gradient(#4a2344 40%,var(--white) 72%)"></div><h4>Grapes</h4><p>$50.00</p></div>
  <div class="abs mini" style="left:791px;top:259px"><div class="pic" role="img" aria-label="Blackberries" style="background:radial-gradient(#1f1a24 40%,var(--white) 72%)"></div><h4>Blackberry</h4><p>$50.00</p></div>
  <div class="abs mini" style="left:791px;top:393px"><div class="pic" role="img" aria-label="Green beans" style="background:radial-gradient(#3e8a2a 36%,var(--white) 70%)"></div><h4>Beans</h4><p>$50.00</p></div>
</section>

<!-- newsletter -->
<section class="abs news">
  <div class="abs news-title">SUBSCRIBE <b>NEWSLETTER</b></div>
  <div class="abs news-input">enter your email address</div>
  <div class="abs btn-green news-btn">SUBSCRIBE <span>⟶</span></div>
</section>

<!-- testimonial -->
<section class="abs testi">
  <h2 class="abs sec-title" style="left:0;width:1026px;top:40px;font-size:30px;letter-spacing:.5px">TESTIMONIAL</h2>
  <div class="abs avatar" role="img" aria-label="Customer portrait" style="left:90px;top:122px"></div>
  <p class="abs quote" style="left:212px;top:126px">"Lorem ipsum dolor sit amet, consectetuer adipiscing elitsed the diam nonummy nibh euismod tincidunt."</p>
  <div class="abs who" style="left:212px;top:250px"><i></i>Jane Doe</div>
  <div class="abs avatar" role="img" aria-label="Customer portrait" style="left:569px;top:122px"></div>
  <p class="abs quote" style="left:689px;top:126px">"Lorem ipsum dolor sit amet, consectetuer adipiscing elitsed the diam nonummy nibh euismod tincidunt."</p>
  <div class="abs who" style="left:689px;top:250px"><i></i>Jane Doe</div>
  <div class="abs arrows" style="left:490px;top:325px"><i>‹</i><i>›</i></div>
</section>

<!-- footer -->
<footer class="abs footer">
  <div class="abs f-logo"><i></i>Brindlecove</div>
  <p class="abs f-desc">Lorem ipsum dolor sit amet, consectetuer adipiscing elit, sed diam nonummy nibh euismod tincidunt ut laoreet dolore magna.</p>
  <div class="abs f-line" style="top:167px"><svg width="10" height="14" viewBox="0 0 10 14"><path d="M5 0a5 5 0 0 1 5 5c0 4-5 9-5 9S0 9 0 5a5 5 0 0 1 5-5z" fill="#fff"/><circle cx="5" cy="5" r="2" fill="#ec1f27"/></svg>42 orchard lane, hillview, united state</div>
  <div class="abs f-line" style="top:194px"><svg width="12" height="9" viewBox="0 0 12 9"><rect width="12" height="9" fill="#fff"/><path d="M0 0 6 5 12 0" fill="none" stroke="#ec1f27"/></svg>contact@brindlecove.com</div>
  <div class="abs f-line" style="top:221px"><svg width="12" height="12" viewBox="0 0 12 12"><circle cx="6" cy="6" r="5.3" fill="none" stroke="#fff" stroke-width="1.3"/><path d="M1 6h10M6 1c-3 3-3 7 0 10M6 1c3 3 3 7 0 10" fill="none" stroke="#fff"/></svg>www.brindlecove.com</div>

  <div class="abs f-head" style="left:437px"><b>INFORMATION</b></div>
  <ul class="abs f-list" style="left:437px;top:84px">
    <li>about our shop</li><li>top sellers</li><li>our blog</li><li>new products</li><li>secure shopping</li>
  </ul>
  <div class="abs f-head" style="left:615px">MY <b>ACCOUNT</b></div>
  <ul class="abs f-list" style="left:615px;top:78px">
    <li>my account</li><li>discount</li><li>personal information</li><li>my address</li><li>order history</li>
  </ul>
  <div class="abs f-head" style="left:876px">PHOTO <b>SNAPGRID</b></div>
  <div class="abs thumb" role="img" aria-label="Fruit photo" style="left:876px;top:105px;background:linear-gradient(135deg,#f29a2e,#c8341f)"></div>
  <div class="abs thumb" role="img" aria-label="Tomato photo" style="left:959px;top:105px;background:linear-gradient(135deg,#b81d1d,#5a1a14)"></div>
  <div class="abs thumb" role="img" aria-label="Vegetable photo" style="left:1042px;top:105px;background:linear-gradient(135deg,#8a5a2a,#e0a040)"></div>
  <div class="abs thumb" role="img" aria-label="Greens photo" style="left:876px;top:185px;background:linear-gradient(135deg,#7dab3a,#d7e8b0)"></div>
  <div class="abs thumb" role="img" aria-label="Produce basket photo" style="left:959px;top:185px;background:linear-gradient(135deg,#c94a2a,#6a8a2a)"></div>
  <div class="abs thumb" role="img" aria-label="Carrots photo" style="left:1042px;top:185px;background:linear-gradient(135deg,#f3f1e8,#e67a2a)"></div>
</footer>

<div class="abs bottom">
  <svg class="abs" style="left:500px;top:-26px" width="200" height="28" viewBox="0 0 200 28"><path d="M0 28C45 28 55 0 100 0s55 28 100 28z" fill="#231f20"/></svg>
  <svg class="abs" style="left:589px;top:-12px" width="22" height="22" viewBox="0 0 22 22"><circle cx="11" cy="11" r="9.5" fill="none" stroke="#fff" stroke-width="1.6"/><path d="M11 16V7M7 10.5 11 6.5l4 4" fill="none" stroke="#fff" stroke-width="1.8"/></svg>
  <div class="abs copy">Copyright © 2018 Brindlecove . All rights reserved.</div>
  <div class="abs pay" style="left:884px;width:74px;background:#3d5b9f"></div>
  <div class="abs pay" style="left:966px;background:#e8a33a"></div>
  <div class="abs pay" style="left:998px;background:#5a7fc8"></div>
  <div class="abs pay" style="left:1030px;background:#2e77bc"></div>
  <div class="abs pay" style="left:1062px;background:#e25a3a"></div>
  <div class="abs pay" style="left:1094px;width:20px;background:#3aa35a"></div>
</div>

</body>
</html>
```